Logo and Graphic Design Project for Children's Event

We need help designing the logo and marketing materials for our summer children's event "The Lantern Crew". This program is for children ages 5-10 and should have a bold, fun feel to it. I would like a strong logo that is the primary feature of the design with additional supporting artwork elements that can be used flexibly in a variety of formats and mediums. I would like the design to capture the overall feel of the event. This event has obstacle course based elements incorporated in to it like the TV Show Galactic Summit Racers but is more focused on the character traits of different warriors throughout history like fearlessness, honor, obedience and respect.

This design will be used for outside marketing and branding and needs to be provided in a vector format. The types of mediums it would be used on is yard signs, banners, door hangers, social media, etc. (Samples of materials for inspiration or from previous events included in the uploaded files.)

Target Market(s)

Families with children ages 5-10

Industry/Entity Type

Religious

Font styles to use
Sans Serif

Requirements
Must have
• - Strong logo that communicates the feel of the event and includes the name "The Lantern Crew".
- Flexible supporting artwork elements that can be used in a variety of mediums.
- Must use fonts that are available from free, open sources or can be provided upon delivery of completed project.
- Must be kid and family friendly
- Event date June 7-11 must be included
- Event time 6:30-8:30pm included
- Include our church logo attached
Nice to have
• - A themed background that could be adapted for use on powerpoint.
Should not have
• - Any content that is scary, violent or not suitable for an audience of children.

```html
<!DOCTYPE html>
<html lang="en">
<head>
<meta charset="utf-8">
<title>The Lantern Crew – June 7-11</title>
<link href="https://fonts.googleapis.com/css2?family=Fredoka:wght@500;600;700&display=swap" rel="stylesheet">
<style>
  :root{
    --sun-yellow:#f3f10a;
    --lime:#c8df12;
    --grass:#9ccd22;
    --deep-green:#3fae34;
    --navy:#2a2478;
    --royal:#1a5fb4;
    --sky-line:#7cc4ee;
    --castle-red:#dd3c1e;
    --plum:#8a1f7a;
    --white:#ffffff;
    --ink:#1a1a1a;
  }
  html,body{margin:0;padding:0;overflow:hidden;background:var(--white);}
  .poster{
    position:relative;width:1200px;height:1024px;overflow:hidden;
    background:radial-gradient(ellipse 900px 820px at 590px 130px, var(--sun-yellow) 0%, var(--lime) 40%, var(--grass) 78%, var(--deep-green) 120%);
    font-family:"Fredoka",sans-serif;
  }
  .scenery{position:absolute;inset:0;width:1200px;height:1024px;}
  .title-text{font-family:"Fredoka",sans-serif;font-weight:700;text-transform:uppercase;}
  .title-back{fill:var(--navy);stroke:var(--navy);stroke-width:22px;stroke-linejoin:round;}
  .title-front{fill:var(--white);stroke:var(--sky-line);stroke-width:8px;stroke-linejoin:round;paint-order:stroke fill;}
  .subtitle{font-family:"Fredoka",sans-serif;font-weight:500;fill:var(--white);letter-spacing:4px;}
  .schedule{font-family:"Fredoka",sans-serif;font-weight:700;fill:var(--white);stroke:var(--plum);stroke-width:13px;stroke-linejoin:round;paint-order:stroke fill;}
  .host{
    position:absolute;left:0;width:1200px;top:890px;
    display:flex;flex-direction:row;justify-content:center;align-items:center;gap:14px;
  }
  .host-mark{width:62px;height:62px;border:2px solid var(--ink);border-radius:50%;box-sizing:border-box;}
  .host-name{font-size:24px;font-weight:500;color:var(--ink);letter-spacing:1px;}
</style>
</head>
<body>
<main class="poster">
  <svg class="scenery" viewBox="0 0 1200 1024" xmlns="http://www.w3.org/2000/svg">
    <defs>
      <radialGradient id="ground-glow" cx="556" cy="860" r="700" gradientUnits="userSpaceOnUse">
        <stop offset="0" stop-color="#f4f10a"/>
        <stop offset="0.55" stop-color="#9ccd22"/>
        <stop offset="1" stop-color="#13a040"/>
      </radialGradient>
      <linearGradient id="cliff-tone" x1="0" y1="0" x2="0" y2="1">
        <stop offset="0" stop-color="#3a8090"/>
        <stop offset="1" stop-color="#5da3bd"/>
      </linearGradient>
      <linearGradient id="figure-tone" x1="0" y1="0" x2="0" y2="1">
        <stop offset="0" stop-color="#2a1f72"/>
        <stop offset="0.7" stop-color="#27308a"/>
        <stop offset="1" stop-color="#1370c8"/>
      </linearGradient>
      <linearGradient id="sun-tone" x1="0" y1="0" x2="1" y2="1">
        <stop offset="0" stop-color="#f5c010"/>
        <stop offset="1" stop-color="#ea8a18"/>
      </linearGradient>
      <linearGradient id="banner-tone" x1="0" y1="0" x2="0" y2="1">
        <stop offset="0" stop-color="#1a4fa4"/>
        <stop offset="1" stop-color="#0a8ad8"/>
      </linearGradient>
    </defs>

    <!-- scenery placeholders -->
    <rect class="cliff-art" role="img" aria-label="Rock climbing cliff face"
      x="0" y="0" width="150" height="964" fill="url(#cliff-tone)"/>
    <rect class="climber-art" role="img" aria-label="Silhouette of a child climbing the cliff"
      x="147" y="72" width="125" height="284" rx="30" fill="url(#figure-tone)"/>

    <polygon class="ground-band" points="0,958 556,834 1200,979 1200,1024 0,1024" fill="url(#ground-glow)"/>

    <rect class="knight-art" role="img" aria-label="Silhouette of a helmeted warrior with sword and shield"
      x="892" y="565" width="208" height="367" rx="40" fill="url(#figure-tone)"/>

    <!-- title lockup -->
    <g class="event-logo" role="img" aria-label="The Lantern Crew">
      <circle class="sun-disc" cx="597" cy="353" r="198" fill="url(#sun-tone)"/>
      <rect class="castle-art" role="img" aria-label="Castle with flag on the sun"
        x="431" y="250" width="334" height="136" fill="var(--castle-red)"/>

      <rect class="title-plate-top" x="490" y="256" width="210" height="112" rx="6" fill="var(--navy)"/>
      <rect class="title-plate-main" x="249" y="388" width="703" height="146" rx="16" fill="var(--navy)"/>
      <polygon class="title-banner" points="249,530 952,530 575,634" fill="url(#banner-tone)"/>

      <text class="title-text title-back" x="597" y="360" text-anchor="middle" font-size="130" textLength="196" lengthAdjust="spacingAndGlyphs">The</text>
      <text class="title-text title-front" x="597" y="360" text-anchor="middle" font-size="130" textLength="196" lengthAdjust="spacingAndGlyphs">The</text>

      <text class="title-text title-back" x="600" y="518" text-anchor="middle" font-size="168" textLength="676" lengthAdjust="spacingAndGlyphs">Lantern</text>
      <text class="title-text title-front" x="600" y="518" text-anchor="middle" font-size="168" textLength="676" lengthAdjust="spacingAndGlyphs">Lantern</text>

      <text class="subtitle" x="588" y="589" text-anchor="middle" font-size="66">CREW</text>
    </g>

    <!-- date and time -->
    <text class="schedule" x="590" y="735" text-anchor="middle" font-size="64" textLength="255" lengthAdjust="spacingAndGlyphs">June 7-11</text>
    <text class="schedule" x="582" y="802" text-anchor="middle" font-size="64" textLength="352" lengthAdjust="spacingAndGlyphs">6.30-8.30 pm</text>
  </svg>

  <div class="host">
    <span class="host-mark"></span>
    <span class="host-name">Harbor Lane Chapel</span>
  </div>
</main>
</body>
</html>
```